Business card for utility of the future

I need a business card template designed for brookvane. We provide sustainable water, energy and waste services to homes.

The card should include name, position, email address, phone number, website and our logo (attached). I would like it to convey professionalism and creativity.

Target Market(s)

Homeowners, investors, corporate partners.

Industry/Entity Type

Utility

Contact Information for Business Card

The card should include name, position, email address, phone number, website and our logo (attached).

```html
<!DOCTYPE html>
<html lang="en">
<head>
<meta charset="utf-8">
<title>brookvane business card</title>
<link rel="stylesheet" href="https://fonts.googleapis.com/css2?family=Tinos:wght@400&family=Arimo:wght@400&display=swap">
<style>
  :root {
    --card-bg: #0b0b0b;
    --card-edge: #1c1c1c;
    --brand-green: #74c08e;
    --text-light: #dadada;
    --icon-glyph: #0b0b0b;
  }
  * { margin: 0; padding: 0; box-sizing: border-box; }
  html, body {
    width: 1200px;
    height: 1200px;
    overflow: hidden;
    background: linear-gradient(180deg, #9d9d9d 0%, #d6d6d6 100%);
  }
  .business-card {
    position: absolute;
    left: 75px;
    top: 300px;
    width: 1050px;
    height: 600px;
    background: var(--card-bg);
    border: 1px solid var(--card-edge);
    box-shadow: 0 18px 40px rgba(0,0,0,0.35);
  }
  .brand-name {
    position: absolute;
    left: 90px;
    top: 262px;
    font-family: "Tinos", serif;
    font-weight: 400;
    font-size: 96px;
    line-height: 1;
    color: var(--text-light);
  }
  .contact-block {
    position: absolute;
    right: 70px;
    top: 150px;
    text-align: right;
  }
  .person-name {
    font-family: "Tinos", serif;
    font-size: 32px;
    color: var(--text-light);
    line-height: 1.1;
    margin-right: 46px;
  }
  .person-role {
    font-family: "Arimo", sans-serif;
    font-size: 20px;
    color: var(--brand-green);
    margin-right: 46px;
    margin-bottom: 34px;
  }
  .contact-list { list-style: none; }
  .contact-item {
    display: flex;
    justify-content: flex-end;
    align-items: center;
    gap: 16px;
    font-family: "Tinos", serif;
    font-size: 26px;
    color: var(--text-light);
    height: 40px;
  }
  .contact-icon {
    width: 28px;
    height: 28px;
    flex: none;
  }
</style>
</head>
<body>
  <section class="business-card">
    <p class="brand-name">brookvane</p>

    <div class="contact-block">
      <p class="person-name">Marcus Hale</p>
      <p class="person-role">Owner</p>
      <ul class="contact-list">
        <li class="contact-item">
          <span>(555) 014-2290</span>
          <svg class="contact-icon" viewBox="0 0 28 28" aria-hidden="true">
            <rect width="28" height="28" rx="3" fill="var(--brand-green)"/>
            <path d="M9 7 l3 0 l1.5 4 l-2 1.5 q1.5 3 4 4 l1.5 -2 l4 1.5 l0 3 q-1 1.5 -3 1.5 q-9 -1 -10 -10 q0 -2 1 -3.5z" fill="var(--icon-glyph)"/>
          </svg>
        </li>
        <li class="contact-item">
          <span>info@brookvane.com</span>
          <svg class="contact-icon" viewBox="0 0 28 28" aria-hidden="true">
            <rect width="28" height="28" rx="3" fill="var(--brand-green)"/>
            <rect x="6" y="9" width="16" height="11" fill="var(--icon-glyph)"/>
            <path d="M6 9 l8 6 l8 -6" stroke="var(--brand-green)" stroke-width="1.5" fill="none"/>
          </svg>
        </li>
        <li class="contact-item">
          <span>www.brookvane.com</span>
          <svg class="contact-icon" viewBox="0 0 28 28" aria-hidden="true">
            <rect width="28" height="28" rx="3" fill="var(--brand-green)"/>
            <circle cx="14" cy="14" r="8" fill="none" stroke="var(--icon-glyph)" stroke-width="2"/>
            <ellipse cx="14" cy="14" rx="3.5" ry="8" fill="none" stroke="var(--icon-glyph)" stroke-width="1.5"/>
            <line x1="6" y1="14" x2="22" y2="14" stroke="var(--icon-glyph)" stroke-width="1.5"/>
          </svg>
        </li>
        <li class="contact-item">
          <span>48 Alder Lane, Fernbrook</span>
          <svg class="contact-icon" viewBox="0 0 28 28" aria-hidden="true">
            <rect width="28" height="28" rx="3" fill="var(--brand-green)"/>
            <path d="M14 6 a6 6 0 0 1 6 6 q0 4 -6 10 q-6 -6 -6 -10 a6 6 0 0 1 6 -6z" fill="var(--icon-glyph)"/>
            <circle cx="14" cy="12" r="2.2" fill="var(--brand-green)"/>
          </svg>
        </li>
      </ul>
    </div>
  </section>
</body>
</html>
```